Established food business needs a new name card design

Refer to attached current name card. Would like a new professional look design with only the company name and logo without any pictures. Would like green and yellow to be included.
To include:
My name "HAKIM RUSLAN" and hand phone number "86207319".
To delete "
"Along Pinegrove Ave 3" and
"www.bu-tirah.com.sg"
To change email to:
"rvk27@tealmail.com.sg"

```html
<!DOCTYPE html>
<html lang="en">
<head>
<meta charset="utf-8">
<title>Bu-Tirah Eating Corner – Name Card</title>
<link rel="stylesheet" href="https://fonts.googleapis.com/css2?family=Lato:wght@400;700&family=Montserrat:wght@500&display=swap">
<style>
  :root {
    --backdrop: #ebebeb;
    --forest: #2a4636;
    --mustard: #e9c935;
    --paper: #ffffff;
    --ink: #444444;
  }
  * { box-sizing: border-box; margin: 0; padding: 0; }
  html, body { width: 1200px; height: 800px; overflow: hidden; }
  body { background: var(--backdrop); position: relative; font-family: "Lato", sans-serif; }

  .card {
    position: absolute;
    left: 316px;
    width: 570px;
    height: 330px;
    border-radius: 24px;
  }
  .card--front { top: 51px; background: var(--forest); }
  .card--back { top: 418px; background: var(--paper); }

  .brand { display: flex; align-items: center; gap: 12px; color: var(--mustard); font-family: "Lato", sans-serif; font-weight: 700; }
  .brand__dot { border-radius: 50%; background: var(--mustard); flex: none; }
  .brand__text { display: flex; flex-direction: column; line-height: 1; }

  .card--front .brand { position: absolute; left: 0; right: 0; top: 122px; justify-content: center; }
  .card--front .brand__dot { width: 70px; height: 70px; }
  .card--front .brand__name { font-size: 44px; letter-spacing: 1px; }
  .card--front .brand__tag { font-size: 13px; letter-spacing: 5px; margin-top: 8px; }

  .address {
    position: absolute; left: 0; right: 0; top: 264px;
    text-align: center; color: var(--mustard); font-size: 14.5px; line-height: 21px;
  }

  .card--back .brand { position: absolute; left: 64px; top: 131px; }
  .card--back .brand__dot { width: 52px; height: 52px; }
  .card--back .brand__name { font-size: 30px; letter-spacing: 0.5px; }
  .card--back .brand__tag { font-size: 9px; letter-spacing: 4px; margin-top: 6px; }

  .divider { position: absolute; left: 283px; top: 126px; width: 2px; height: 77px; background: var(--forest); }

  .contact { position: absolute; left: 311px; top: 128px; }
  .contact__name { font-family: "Montserrat", sans-serif; font-weight: 500; font-size: 16px; color: var(--forest); letter-spacing: 0.5px; }
  .contact__line { display: flex; align-items: center; gap: 8px; margin-top: 10px; font-size: 14px; color: var(--ink); }
  .contact__line + .contact__line { margin-top: 5px; }
  .contact__icon { width: 11px; height: 11px; fill: var(--forest); flex: none; }
</style>
</head>
<body>
  <section class="card card--front">
    <div class="brand">
      <span class="brand__dot"></span>
      <span class="brand__text">
        <span class="brand__name">BU-TIRAH</span>
        <span class="brand__tag">EATING CORNER</span>
      </span>
    </div>
    <p class="address">18 Senoko Craft Lane 4 # 02-07<br>Singapore 728841</p>
  </section>

  <section class="card card--back">
    <div class="brand">
      <span class="brand__dot"></span>
      <span class="brand__text">
        <span class="brand__name">BU-TIRAH</span>
        <span class="brand__tag">EATING CORNER</span>
      </span>
    </div>
    <div class="divider"></div>
    <div class="contact">
      <p class="contact__name">HAKIM RUSLAN</p>
      <p class="contact__line">
        <svg class="contact__icon" viewBox="0 0 24 24" aria-hidden="true"><path d="M6.6 10.8a15.1 15.1 0 0 0 6.6 6.6l2.2-2.2c.3-.3.7-.4 1-.2 1.1.4 2.3.6 3.6.6.6 0 1 .4 1 1V20c0 .6-.4 1-1 1A17 17 0 0 1 3 4c0-.6.4-1 1-1h3.5c.6 0 1 .4 1 1 0 1.3.2 2.5.6 3.6.1.3 0 .7-.2 1z"/></svg>
        86207319
      </p>
      <p class="contact__line">
        <svg class="contact__icon" viewBox="0 0 24 24" aria-hidden="true"><path d="M2 4h20v16H2z M4 6v.5l8 6 8-6V6z" fill-rule="evenodd"/></svg>
        rvk27@tealmail.com.sg
      </p>
    </div>
  </section>
</body>
</html>
```